Corwell Holdings Business Cards

Hello. I need business cards designed with our new logo. I'd like to see at least 3 different designs. At least one with a dark background, and at least one with a white background. Maybe one with gray or blue for the background. Play with gradient colors and maybe even insert a pic of a skyline in the background of one or more of them. Use your judgement. We will need 2 cards printed. They need to accommodate the employee name, title, company address, phone, email, and website. Thanks.

Target Market(s)

Wealthy mature investors.

Contact Information for Business Card

Single-sided, professional, clean design that incorporates our logo.

Font styles to use
Sans Serif

Requirements
Must have
• Our new logo needs to be featured on it. (See attached.)
• Employee Name (In all CAPS)
• Title
• Street Address, City, ST Zip Code
• Cell Phone #, Email Address, Website Address
Nice to have
• Design that blends well with our new logo and its colors, or a city scape or other graphic design that looks like an apartment complex in the background. Blues and grays are nice, but use your judgement.
Should not have
• Modern or oriental looking designs or bright colors.

```html
<!DOCTYPE html>
<html lang="en">
<head>
<meta charset="utf-8">
<title>Corwell Holdings Business Cards</title>
<link rel="stylesheet" href="https://fonts.googleapis.com/css2?family=Montserrat:wght@500;600&family=Open+Sans:wght@400;700&display=swap">
<style>
  :root {
    --stage: #2b2b2b;
    --card-dark: #4d4d4f;
    --glow: #29a8e0;
    --brand-blue: #29a3dc;
    --ink: #333333;
    --band-gray: #4a4a4c;
    --white: #ffffff;
  }
  * { box-sizing: border-box; margin: 0; padding: 0; }
  html, body { width: 1200px; height: 895px; overflow: hidden; }
  body {
    background: var(--stage);
    font-family: "Open Sans", sans-serif;
    position: relative;
  }
  .card {
    position: absolute;
    left: 290px;
    width: 620px;
    height: 354px;
    overflow: hidden;
    box-shadow: 0 10px 30px rgba(0,0,0,.45);
  }
  /* Front (dark) */
  .card--front {
    top: 60px;
    background:
      radial-gradient(ellipse 46% 52% at 52% 50%, var(--glow) 0%, rgba(41,168,224,.55) 35%, rgba(77,77,79,0) 80%),
      var(--card-dark);
  }
  .front__map {
    position: absolute;
    left: 70px; top: 40px; width: 480px; height: 270px;
    background: radial-gradient(ellipse at center, rgba(255,255,255,.12), rgba(255,255,255,0) 70%);
  }
  .brand {
    position: absolute;
    display: flex;
    align-items: center;
    gap: 14px;
    font-family: "Montserrat", sans-serif;
    font-weight: 600;
    letter-spacing: .04em;
    text-transform: uppercase;
    white-space: nowrap;
  }
  .brand__square { display: block; flex: none; }
  .card--front .brand {
    left: 0; right: 0; top: 150px;
    justify-content: center;
    color: var(--white);
    font-size: 34px;
  }
  .card--front .brand__square { width: 40px; height: 40px; background: var(--white); }

  /* Back (white) */
  .card--back {
    top: 474px;
    background: var(--white);
  }
  .card--back .brand {
    right: 40px; top: 52px;
    color: var(--brand-blue);
    font-size: 22px;
  }
  .card--back .brand__square { width: 26px; height: 26px; background: var(--brand-blue); }

  .person {
    position: absolute;
    left: 44px; top: 138px;
  }
  .person__name {
    font-family: "Open Sans", sans-serif;
    font-weight: 700;
    font-size: 28px;
    color: var(--brand-blue);
    line-height: 1.1;
    letter-spacing: .01em;
  }
  .person__title {
    font-size: 15px;
    color: var(--ink);
    margin-top: 2px;
  }
  .contact {
    list-style: none;
    margin-top: 14px;
  }
  .contact__item {
    display: flex;
    align-items: center;
    gap: 10px;
    font-size: 15px;
    color: var(--ink);
    line-height: 26px;
    white-space: nowrap;
  }
  .contact__item svg { width: 14px; height: 14px; flex: none; }
  .contact__accent { color: var(--brand-blue); }
  .back__bands {
    position: absolute;
    left: 0; bottom: 0;
    width: 620px; height: 60px;
  }
</style>
</head>
<body>

  <section class="card card--front" aria-label="Card front">
    <div class="front__map" role="img" aria-label="Faint dotted world map"></div>
    <div class="brand">
      <span class="brand__square"></span>
      <span class="brand__name">Corwell Holdings, LLC</span>
    </div>
  </section>

  <section class="card card--back" aria-label="Card back">
    <div class="brand">
      <span class="brand__square"></span>
      <span class="brand__name">Corwell Holdings, LLC</span>
    </div>

    <div class="person">
      <h1 class="person__name">DANIEL MERCER</h1>
      <p class="person__title">Managing Director</p>
      <ul class="contact">
        <li class="contact__item">
          <svg viewBox="0 0 16 16" aria-hidden="true"><path fill="#29a3dc" d="M3.5 1.5l2.5 0 1 3.5-1.6 1.2a9 9 0 0 0 4.4 4.4L11 9l3.5 1v2.5c0 1-1 2-2 2A11 11 0 0 1 1.5 3.5c0-1 1-2 2-2z"/></svg>
          <span>000-000-0000</span>
        </li>
        <li class="contact__item">
          <svg viewBox="0 0 16 16" aria-hidden="true"><rect x="1" y="3" width="14" height="10" rx="1" fill="#29a3dc"/><path d="M1.5 3.5L8 9l6.5-5.5" fill="none" stroke="#fff" stroke-width="1.3"/></svg>
          <span>daniel@<span class="contact__accent">corwellholdings</span>.com</span>
        </li>
        <li class="contact__item">
          <svg viewBox="0 0 16 16" aria-hidden="true"><g fill="none" stroke="#29a3dc" stroke-width="1.4"><circle cx="8" cy="8" r="6.3"/><ellipse cx="8" cy="8" rx="2.8" ry="6.3"/><path d="M1.7 8h12.6M2.8 4.7h10.4M2.8 11.3h10.4"/></g></svg>
          <span>www.<span class="contact__accent">corwellholdings</span>.com</span>
        </li>
        <li class="contact__item">
          <svg viewBox="0 0 16 16" aria-hidden="true"><path fill="#29a3dc" d="M8 1a5 5 0 0 0-5 5c0 3.8 5 9 5 9s5-5.2 5-9a5 5 0 0 0-5-5zm0 7a2 2 0 1 1 0-4 2 2 0 0 1 0 4z"/></svg>
          <span>1200 Larimer Street, Denver, CO 80202</span>
        </li>
      </ul>
    </div>

    <svg class="back__bands" viewBox="0 0 620 60" aria-hidden="true">
      <polygon points="0,46 420,46 428,60 0,60" fill="var(--band-gray)"/>
      <polygon points="400,18 620,18 620,60 428,60 400,28" fill="var(--brand-blue)"/>
    </svg>
  </section>

</body>
</html>
```